Smart, intuitive SaaS software dashboard design

PactBloom is an innovative modern SaaS (software as a service) solution for contract and meeting management.

What we are looking for is fresh ideas for our dashboard. We do not need web coding or actionable wireframes now – but purely great design ideas from where to continue forward.

How should a modern web software dashboard look like? Fresh, intuitive, easy-to-use, and adaptable for responsive mobile designs. We hope that when the user logs into the service and sees the dashboard, he/she gets a good big picture of the current status of the most important documents of his/hers company.

To get to know the service and see the components, we kindly ask you to register to our service at www.pactbloom-demo.net and to utilize the free trial (30 days) so you can see the existing dashboard live. And also try out how it works. Might help you to get ideas how to improve it.

(The designer we will choose might be offered later on to design some other pages as well (contract view and edit pages, meeting page etc).)

You’ll find additional information in the attachment.

You’ll find more information of the company and the service also at www.pactbloom-demo.net

Target Market(s)

Global

Industry/Entity Type

Business Management

Number of Pages Required

1 page

Font styles to use
Sans Serif

Requirements
Must have
• 1) Clear design idea for us to iterate from, 2) Modern look and feel - elegant & bold at the same time - still with credibility in our target group. And 3) Suitable for dashboard usage - it should it a clear big picture for the user.
• UPDATE:
• Users should see most important things with one glance. Therefore we would like to see AT LEAST these items mentioned below on the first page.
• NOTE: if all these things are visible on the dashboard, the menu list is maybe not needed on the left. (And there might be some icons on the top header with needed settings/inbox features anyway.)
• NOTE2: as explained earlier, the design should be responsive i.e. work without modifications in PC, iPad and mobile (the areas/boxes would just rearrange themselves on top of each other.)
• -First area should be Documents, which would include different document categories: Contracts, Finance & Admin and HR
• -All different types of Meetings could be the next area (upcoming ones clearly visible with date and maybe description, time and location visible also).
• -Reminders and Activity Feed (they might also be together in top of each other, so that Reminder is visible first and Activity feed can be chosen from the tab.)
• -Virtual Datarooms (maybe 1-3 different ones with some analytics for each visible e.g. like usage/visits per day)
• Saved searches in very important list as users can save their most important searches. There are typically many of these, so at least 5 should be visible and then see all button (maybe even more could be visible if they fit on your design)
• My Latest is also important.
• (As explained, Action Required area is NOT needed anymore).
Nice to have
• Surprise us!
Should not have
• Please avoid the boring traditional legacy stuff and the common report dashboards.
• You do not need design a 100% mockup for the techie to continue with. The ideas count.

```html
<!DOCTYPE html>
<html lang="en">
<head>
<meta charset="utf-8">
<title>PactBloom Dashboard</title>
<link href="https://fonts.googleapis.com/css2?family=Open+Sans:wght@300;400;600;700&display=swap" rel="stylesheet">
<style>
:root{
  --bg-deep:#06121d;
  --bg-mid:#0f3550;
  --sidebar:#263a4e;
  --sidebar-active:#2e4459;
  --icon-box:#34495e;
  --green:#7cc800;
  --green-text:#6fbf00;
  --meeting:#4d6782;
  --white:#ffffff;
  --muted:#b8c4cf;
  --navy:#1e3a5c;
  --grey-text:#777;
  --dark:#0f1a22;
}
*{margin:0;padding:0;box-sizing:border-box}
html,body{width:1200px;height:866px;overflow:hidden}
body{
  font-family:"Open Sans",sans-serif;
  background:radial-gradient(ellipse at 60% 20%,var(--bg-mid) 0%,#0a2234 40%,var(--bg-deep) 100%);
  position:relative;color:var(--white);
}
.abs{position:absolute}
.brand{left:152px;top:26px;display:flex;align-items:center;gap:8px}
.brand-dot{width:32px;height:32px;border-radius:50%;background:var(--green)}
.brand-name{font-size:17px;font-weight:400;letter-spacing:1px;color:var(--white)}
.dashboard{left:148px;top:79px;width:902px;height:741px}
.sidebar{left:0;top:0;width:273px;height:741px;background:var(--sidebar)}
.search{left:13px;top:15px;width:187px;height:38px;border:2px solid #6d7f90;border-radius:19px}
.search svg{position:absolute;left:16px;top:12px}
.search-label{position:absolute;right:14px;top:9px;font-size:11px;color:var(--muted)}
.add-btn{left:207px;top:0;width:66px;height:63px;background:var(--green)}
.add-btn svg{position:absolute;left:21px;top:20px}
.avatar{left:18px;top:110px;width:92px;height:92px;border-radius:50%;background:linear-gradient(160deg,#e8d6c8,#b89478);border:3px solid #fff}
.profile-name{left:123px;top:137px;font-size:12px;font-weight:700}
.profile-role{left:123px;top:156px;font-size:12px;color:var(--muted)}
.nav-item{left:0;height:28px;width:273px;display:flex;align-items:center}
.nav-icon{width:30px;height:28px;background:var(--icon-box);display:flex;align-items:center;justify-content:center}
.nav-label{margin-left:18px;font-size:12px;color:var(--muted);font-weight:300}
.nav-group{left:0;top:429px;width:273px;height:74px;background:var(--sidebar-active);padding:13px 0 0 44px;font-size:12px;line-height:18px;color:var(--muted);font-weight:300}
.nav-group b{color:#fff;font-weight:600}
.meeting{left:273px;top:0;width:314px;height:288px;background:linear-gradient(135deg,#5a7590 0%,var(--meeting) 50%,#3d566f 100%)}
.panel-title{font-size:15px;font-weight:700;letter-spacing:.3px}
.rule{height:1px;background:rgba(255,255,255,.8)}
.meet-label{font-size:12.5px;font-weight:300}
.date-row{display:flex;align-items:center;gap:10px;font-size:12.5px;font-weight:300}
.pill{width:86px;height:28px;border-radius:14px;background:var(--green);font-size:12px;text-align:center;line-height:28px;color:var(--white)}
.photo-team{left:587px;top:0;width:315px;height:288px;background:linear-gradient(120deg,#b9bcc2 0%,#e4e6ea 35%,#5b6472 60%,#d8dadd 100%)}
.reminder{left:273px;top:288px;width:314px;height:299px;background:var(--green)}
.rem-item{left:35px;width:275px;font-size:12px;line-height:15px;color:#f1fbe3;font-weight:300;white-space:nowrap}
.rem-item b{color:var(--dark);font-weight:700}
.rem-meta{left:35px;display:flex;align-items:center;gap:5px;font-size:7.5px;color:var(--dark)}
.rem-meta span+svg{margin-left:14px}
.photo-tablet{left:273px;top:587px;width:314px;height:154px;background:linear-gradient(135deg,#3a3f47 0%,#6d7178 45%,#c9b9a8 100%)}
.feed{left:587px;top:288px;width:315px;height:453px;background:var(--white);color:var(--grey-text)}
.feed .panel-title{color:#333}
.feed-rule{height:1px;background:#444}
.feed-item{left:25px;display:flex;gap:9px}
.feed-avatar{width:53px;height:49px;background:linear-gradient(150deg,#caa58a,#6b5546);flex:none}
.feed-text{width:225px;font-size:11.5px;line-height:17px;font-weight:300;white-space:nowrap}
.feed-text b{color:var(--navy);font-weight:600;font-size:12.5px}
.feed-time{font-size:9px;line-height:12px;color:var(--green-text);margin-top:2px}
.see-all{left:29px;top:399px;width:266px;height:37px;border:2px solid #ccc;border-radius:19px;text-align:center;line-height:33px;color:var(--green-text);font-size:12px}
.copyright{left:0;width:1200px;top:841px;text-align:center;font-size:8px;color:#fff;padding-left:28px}
</style>
</head>
<body>
<div class="abs brand"><span class="brand-dot"></span><span class="brand-name">PACTBLOOM</span></div>

<main class="abs dashboard">
  <aside class="abs sidebar">
    <div class="abs search">
      <svg width="12" height="12" viewBox="0 0 12 12"><circle cx="5" cy="5" r="3.5" fill="none" stroke="#c9d2da" stroke-width="1.6"/><line x1="7.5" y1="7.5" x2="10.5" y2="10.5" stroke="#c9d2da" stroke-width="1.8"/></svg>
      <span class="search-label">Contract ▾</span>
    </div>
    <div class="abs add-btn"><svg width="24" height="24" viewBox="0 0 24 24"><path d="M12 2v20M2 12h20" stroke="#fff" stroke-width="1.6"/></svg></div>
    <div class="abs avatar" role="img" aria-label="Profile photo of the user"></div>
    <div class="abs profile-name">Euismod Tincidunt</div>
    <div class="abs profile-role">Smart digital services ▾</div>

    <div class="abs nav-item" style="top:232px"><span class="nav-icon"><svg width="13" height="13" viewBox="0 0 13 13"><rect x="1.5" y="1.5" width="8" height="10" fill="none" stroke="#fff"/><path d="M4 5h4M4 8h3" stroke="#fff"/></svg></span><span class="nav-label">Contracts</span></div>
    <div class="abs nav-item" style="top:273px"><span class="nav-icon"><svg width="14" height="14" viewBox="0 0 14 14"><circle cx="7" cy="7" r="5.5" fill="none" stroke="#fff"/><text x="7" y="10" font-size="8" text-anchor="middle" fill="#fff" font-family="sans-serif">$</text></svg></span><span class="nav-label">Finance &amp; Admin</span></div>
    <div class="abs nav-item" style="top:313px"><span class="nav-icon"><svg width="14" height="14" viewBox="0 0 14 14"><circle cx="8.5" cy="5.5" r="4" fill="none" stroke="#fff"/><line x1="5.5" y1="8.5" x2="1.5" y2="12.5" stroke="#fff" stroke-width="1.5"/></svg></span><span class="nav-label">HR</span></div>
    <div class="abs nav-item" style="top:353px"><span class="nav-icon"><svg width="12" height="14" viewBox="0 0 12 14"><rect x="1.5" y="1" width="9" height="12" fill="none" stroke="#fff"/><path d="M3.5 4h5M3.5 7h5M3.5 10h5" stroke="#fff"/></svg></span><span class="nav-label">Company Register</span></div>
    <div class="abs nav-item" style="top:394px"><span class="nav-icon"><svg width="16" height="12" viewBox="0 0 16 12"><path d="M2 10a6 6 0 0 1 12 0z" fill="none" stroke="#fff"/><path d="M5 10V7M8 10V5M11 10V7" stroke="#fff"/></svg></span><span class="nav-label">Virtual Data Rooms</span></div>
    <div class="abs nav-group"><b>Meetings</b><br>Board Meeting<br>Shareholders' Meeting</div>
    <div class="abs nav-item" style="top:513px"><span class="nav-icon"><svg width="12" height="12" viewBox="0 0 12 12"><circle cx="5" cy="5" r="3.5" fill="none" stroke="#fff" stroke-width="1.6"/><line x1="7.5" y1="7.5" x2="10.5" y2="10.5" stroke="#fff" stroke-width="1.8"/></svg></span><span class="nav-label">Saved searches</span></div>
    <div class="abs nav-item" style="top:554px"><span class="nav-icon"><svg width="12" height="14" viewBox="0 0 12 14"><path d="M1.5 1h6l3 3v9h-9z" fill="none" stroke="#fff"/><path d="M3.5 7h5M3.5 10h5" stroke="#fff"/></svg></span><span class="nav-label">My latest</span></div>
  </aside>

  <section class="abs meeting" role="img" aria-label="Business meeting scene behind a blue overlay">
    <div class="abs panel-title" style="left:35px;top:23px;color:var(--green)">MEETING</div>
    <div class="abs rule" style="left:35px;top:49px;width:241px"></div>
    <div class="abs meet-label" style="left:37px;top:73px">Board Meetings</div>
    <div class="abs date-row" style="left:37px;top:96px"><svg width="18" height="18" viewBox="0 0 18 18"><rect x="1" y="3" width="16" height="14" fill="none" stroke="#fff"/><path d="M1 6h16M5 1v4M13 1v4" stroke="#fff"/><path d="M4 9h10M4 12h10M4 15h10" stroke="#fff" stroke-dasharray="1.5 1.5"/></svg>27th June,2016</div>
    <div class="abs date-row" style="left:37px;top:131px"><svg width="18" height="18" viewBox="0 0 18 18"><rect x="1" y="3" width="16" height="14" fill="none" stroke="#fff"/><path d="M1 6h16M5 1v4M13 1v4" stroke="#fff"/><path d="M4 9h10M4 12h10M4 15h10" stroke="#fff" stroke-dasharray="1.5 1.5"/></svg>16th Aug,2016</div>
    <div class="abs pill" style="left:189px;top:92px">SEE ALL</div>
    <div class="abs pill" style="left:189px;top:126px">ADD</div>
    <div class="abs meet-label" style="left:37px;top:189px">Shareholders' Meetings</div>
    <div class="abs date-row" style="left:37px;top:212px"><svg width="18" height="18" viewBox="0 0 18 18"><rect x="1" y="3" width="16" height="14" fill="none" stroke="#fff"/><path d="M1 6h16M5 1v4M13 1v4" stroke="#fff"/><path d="M4 9h10M4 12h10M4 15h10" stroke="#fff" stroke-dasharray="1.5 1.5"/></svg>04th Aug,2016</div>
    <div class="abs pill" style="left:189px;top:208px">SEE ALL</div>
    <div class="abs pill" style="left:189px;top:242px">ADD</div>
  </section>

  <div class="abs photo-team" role="img" aria-label="Photo of business people in suits talking"></div>

  <section class="abs reminder">
    <div class="abs panel-title" style="left:37px;top:24px">REMINDER</div>
    <div class="abs rule" style="left:37px;top:47px;width:240px"></div>

    <p class="abs rem-item" style="top:72px"><b>Lorem ipsum</b> dolor sit amet, consectetuer<br>adipiscing elit, sed diam nonummy nibh euismod</p>
    <div class="abs rem-meta" style="top:112px"><svg width="10" height="10" viewBox="0 0 10 10"><rect x=".5" y="1.5" width="9" height="8" fill="none" stroke="#fff"/><path d="M.5 3.5h9" stroke="#fff"/></svg><span>23th June,2016</span><svg width="9" height="9" viewBox="0 0 9 9"><circle cx="4.5" cy="4.5" r="3.8" fill="none" stroke="#fff"/><path d="M4.5 2v2.5h2" stroke="#fff" fill="none"/></svg><span>11:00am</span></div>

    <p class="abs rem-item" style="top:147px"><b>Ut wisi enim ad</b> minim veniam, quis nostrud<br>exerci tation ullamcorper suscipit lobortis nisl</p>
    <div class="abs rem-meta" style="top:187px"><svg width="10" height="10" viewBox="0 0 10 10"><rect x=".5" y="1.5" width="9" height="8" fill="none" stroke="#fff"/><path d="M.5 3.5h9" stroke="#fff"/></svg><span>23th June,2016</span><svg width="9" height="9" viewBox="0 0 9 9"><circle cx="4.5" cy="4.5" r="3.8" fill="none" stroke="#fff"/><path d="M4.5 2v2.5h2" stroke="#fff" fill="none"/></svg><span>11:00am</span></div>

    <p class="abs rem-item" style="top:221px"><b>Claritas est</b> etiam processus dynamicus, qui<br>sequitur mutationem consuetudium lectorum.</p>
    <div class="abs rem-meta" style="top:261px"><svg width="10" height="10" viewBox="0 0 10 10"><rect x=".5" y="1.5" width="9" height="8" fill="none" stroke="#fff"/><path d="M.5 3.5h9" stroke="#fff"/></svg><span>23th June,2016</span><svg width="9" height="9" viewBox="0 0 9 9"><circle cx="4.5" cy="4.5" r="3.8" fill="none" stroke="#fff"/><path d="M4.5 2v2.5h2" stroke="#fff" fill="none"/></svg><span>11:00am</span></div>
  </section>

  <div class="abs photo-tablet" role="img" aria-label="Photo of a hand tapping a tablet point-of-sale screen"></div>

  <section class="abs feed">
    <div class="abs panel-title" style="left:25px;top:24px">ACTIVITY FEED</div>
    <div class="abs feed-rule" style="left:25px;top:48px;width:243px"></div>

    <div class="abs feed-item" style="top:73px"><div class="feed-avatar" role="img" aria-label="Profile photo"></div><div class="feed-text"><b>Jare vitanane creared</b> "vel illum dolore<br>eu feugiat nulla" employment<div class="feed-time">23th June,2016<br>01:20pm</div></div></div>
    <div class="abs feed-item" style="top:152px"><div class="feed-avatar" role="img" aria-label="Profile photo"></div><div class="feed-text"><b>Jare vitanane creared</b> "vel illum dolore<br>eu feugiat nulla" employment<div class="feed-time">23th June,2016<br>01:20pm</div></div></div>
    <div class="abs feed-item" style="top:231px"><div class="feed-avatar" role="img" aria-label="Profile photo"></div><div class="feed-text"><b>Jare vitanane creared</b> "vel illum dolore<br>eu feugiat nulla" employment<div class="feed-time">23th June,2016<br>01:20pm</div></div></div>
    <div class="abs feed-item" style="top:310px"><div class="feed-avatar" role="img" aria-label="Profile photo"></div><div class="feed-text"><b>Jare vitanane creared</b> "vel illum dolore<br>eu feugiat nulla" employment<div class="feed-time">23th June,2016<br>01:20pm</div></div></div>

    <div class="abs see-all">SEE ALL</div>
  </section>
</main>

<footer class="abs copyright">Copyright © 2016 pactbloom</footer>
</body>
</html>
```